Relaunch of company website (Technical company)

Hi all,

we need a website based on Wordpress who makes the customer curious and excited of all the possibilities we can offer.
Customers are B2B. The layout should be based on the screenshots I added, but refreshed and modernized with some nice gadgets.
All needs to be responsive for the different devices.
We are a technical company. We provide a full range of service from 3D scan, Manufacturing, Prototyping, Bulk production and CAD service.

Later the website needs to have a multi language option.

Home:

1. Logo top left (attached)
2. Menu bar top right
3. Header picture like in the screenshot
4. Than the three small blue pics (CAD - Fertigung - Manufaktur) we want a
hoover-small zoom effect as soon as the mouse hits them.
5. Introduction text of our company
6. Contact Information (Design sample see attachment)
7. At the end "Impressum - Datenschutzerklärung - Haftungsausschluss. Those need to be linked to extra pages where we can add mandatory text (Legal notice, Privacy, Disclaimer)

Leistungen - Our service:

1. See the attachment named our service.
2. First on page a gallery where we can add pictures. If moving the mouse over the picture we want a one line explanation e.g. 3D Scan, Production, Die cast...
no click option at the pictures, just to see.
3. Below that, a side menu (we need to add or remove items by our self if necessary) on the left where we can add our service.
4. If the customer is clicking a service, it needs to be highlighted
5. After clicking a service we want our text to that service appear right of the menu (see attachment sample) and 2 big pictures on top of the menu and text field.

Gallery:

1. Headline pictures for each gallery Category (6-8 at the moment)
2. Mouse over the picture zooms it a little in and adds a text what category it is
e.g. Reverse engineering, Prototyping, Laserscan
3. Clicking on the picture opens the detail gallery to that category. There we need
to add pictures specific to that service.
4. If the customer is clicking on a picture from there, all pictures from that
Category will open in a full screen view mode

Blog:

1. A blog to add news (picture and text). Right now we don´t have the time to feed
it, so we want to deactivate it as long as we cant keep it up to date. Later it
should be part of the website.

Unternehmen:

1. Drop down menu: Our Team - History - Unsere Partner - AGB - Impressum

Our Team:
1. Short description of our employees including picture (see attachment)
2. Contact Information (Design sample see attachment)
3. At the end "Impressum - Datenschutzerklärung - Haftungsausschluss. Those need to be linked to extra pages where we can add mandatory text (Legal notice, Privacy, Disclaimer)

History:
1. Timeline where we can add milestones including date, and pictures of the company (see screenshot)

Unsere Partner:
1. Text field where we can introduce our partners including pictures if necessary.

A blog would be a nice option, social media shortcuts to Lumigrid-QZ but no preview of QZ Timeline within the website.

We do have professional text already, that will be added by us. We expect you to use any sample text and pictures for the draft, beside what we supply already.

If you see the need of buying pictures from Pixvane or any other picture company that is OK for us.

What we expect:

A modern, fresh website based on our existing design, changes are fine as long as the whole website design does not change completely to an unicorn thing in pink. Feel free to be creative. New ideas will be discussed, we are open to good ideas. We don´t stick fix to our idea, but we want our customers can see that its still the same company.
Scrolling effects would be a nice gadget if possible.

We have a bad page already...don´t want a second bad one :-)

Our company blue is RBG 106, 206, 224

Greets to all, looking for professional results.

Target Market(s)

B2B, Engineering companys,

Industry/Entity Type

Technical Service

Number of Pages Required

5+ page

Font styles to use
Sans Serif
Other font styles liked:
• verdana

Colors
0455a3
000000
ffffff

Requirements
Must have
• Responsive design, We want to be able to add posts to the Blog, pictures to the categories, and categories by ourself if necessary. (Wordpress)
• Lets say we want to add one more category at „Leistungen-Our Service“ that should be possible for us in the wordpress background.
Nice to have
• Dynamic elements to make the website more alive.
Should not have
• Sliders, Contact form

```html
<!DOCTYPE html>
<html lang="en">
<head>
<meta charset="utf-8">
<title>Veltra Precision – Our Partner</title>
<link href="https://fonts.googleapis.com/css2?family=Jost:wght@500;600;700&family=Questrial&family=Montserrat:wght@600;700&display=swap" rel="stylesheet">
<style>
  :root {
    --brand-blue: #0455a3;
    --ink: #111111;
    --body-grey: #6b6b6b;
    --soft-grey: #999999;
    --panel-grey: #f3f3f3;
    --white: #ffffff;
  }
  * { margin: 0; padding: 0; box-sizing: border-box; }
  html, body { width: 1110px; height: 1200px; overflow: hidden; background: var(--white); }
  body { position: relative; font-family: "Questrial", sans-serif; color: var(--body-grey); }

  .site-header { position: absolute; left: 0; top: 0; width: 1110px; height: 70px; background: var(--brand-blue); }
  .brand { position: absolute; left: 149px; top: 16px; display: flex; align-items: center; gap: 8px;
    font-family: "Questrial", sans-serif; font-size: 22px; color: var(--white); letter-spacing: 0.5px; }
  .brand-mark { width: 12px; height: 12px; background: var(--white); }
  .main-nav { position: absolute; top: 29px; left: 0; width: 100%; }
  .main-nav a { position: absolute; font-family: "Montserrat", sans-serif; font-weight: 700; font-size: 9px;
    letter-spacing: 1.2px; color: var(--white); text-decoration: none; white-space: nowrap; }
  .nav-lang svg { margin-left: 5px; vertical-align: middle; }

  .section-title { position: absolute; left: 0; width: 1110px; text-align: center; font-family: "Jost", sans-serif;
    font-weight: 700; font-size: 24px; letter-spacing: 5.5px; color: var(--ink); }
  .title-bar { position: absolute; left: 540px; width: 30px; height: 6px; background: var(--brand-blue); }

  .partner-photo { position: absolute; width: 265px; height: 228px;
    background: radial-gradient(ellipse at 55% 95%, #bfefff 0%, #2f8fd8 18%, #0b3a7a 45%, #04152e 80%);
    box-shadow: 0 12px 28px rgba(0, 0, 0, 0.35), 0 18px 30px rgba(40, 140, 230, 0.18); }

  .partner-text { position: absolute; width: 444px; }
  .partner-text.align-right { text-align: right; }
  .partner-name { font-family: "Jost", sans-serif; font-weight: 600; font-size: 13.5px; color: var(--ink); }
  .partner-tag { margin-top: 14px; font-family: "Jost", sans-serif; font-weight: 600; font-size: 11px;
    color: var(--brand-blue); letter-spacing: 0.3px; }
  .partner-copy { margin-top: 11px; font-size: 11.3px; line-height: 17.5px; }
  .partner-copy + .partner-copy { margin-top: 17px; }

  .contact-band { position: absolute; left: 0; top: 786px; width: 1110px; height: 372px; background: var(--panel-grey); }
  .contact-tab { position: absolute; left: 526px; top: 944px; width: 54px; text-align: center;
    font-family: "Montserrat", sans-serif; font-weight: 600; font-size: 8.5px; letter-spacing: 0.5px;
    color: var(--brand-blue); padding-bottom: 10px; border-bottom: 1.5px solid var(--brand-blue); }
  .contact-details { position: absolute; left: 0; top: 988px; width: 1110px; text-align: center;
    font-family: "Montserrat", sans-serif; font-weight: 600; font-size: 7.8px; letter-spacing: 1px; color: var(--soft-grey); }
  .contact-details p { line-height: 10px; }
  .contact-details .gap { margin-top: 7px; }
  .contact-details .gap-lg { margin-top: 11px; }
  .contact-details strong { color: #333333; font-weight: 600; }

  .site-footer { position: absolute; left: 0; top: 1158px; width: 1110px; height: 42px; background: var(--brand-blue);
    display: flex; align-items: center; justify-content: center; font-family: "Montserrat", sans-serif;
    font-weight: 700; font-size: 9px; letter-spacing: 1px; color: var(--white); }
  .site-footer .sep { margin: 0 12px; }
</style>
</head>
<body>
  <header class="site-header">
    <div class="brand"><span class="brand-mark"></span>Veltra Precision</div>
    <nav class="main-nav">
      <a style="left:586px">HOME</a>
      <a style="left:654px">LEISTUNGEN</a>
      <a style="left:751px">GALERIE</a>
      <a style="left:830px">UNTERNEHMEN</a>
      <a class="nav-lang" style="left:936px">EN<svg width="7" height="4" viewBox="0 0 7 4"><path d="M0 0h7L3.5 4z" fill="#fff"/></svg></a>
    </nav>
  </header>

  <h1 class="section-title" style="top:138px">OUR PARTNER</h1>
  <div class="title-bar" style="top:184px"></div>

  <div class="partner-photo" style="left:149px; top:232px" role="img" aria-label="Welder in protective mask with bright blue sparks"></div>
  <div class="partner-text" style="left:454px; top:256px">
    <h2 class="partner-name">Lorem Ipsum Dolor Sit Amet</h2>
    <h3 class="partner-tag">DUIS AUTE IRURE DOLOR</h3>
    <p class="partner-copy">Lorem ipsum dolor sit amet, consectetur adipiscing elit, sed do eiusmod tempor incid-idunt ut labore et dolore magna aliqua. Ut enim ad minim veniam, quis nostrud exer-citation ullamco laboris nisi ut aliquip ex ea commodo consequat.</p>
    <p class="partner-copy">Duis aute irure dolor in reprehenderit in voluptate velit esse cillum dolore eu fugiat nulla pariatur. Excepteur sint occaecat cupidatat non proident, sunt in culpa qui officia deserunt mollit anim id est laborum</p>
  </div>

  <div class="partner-text align-right" style="left:210px; top:512px">
    <h2 class="partner-name">Lorem Ipsum Dolor Sit Amet</h2>
    <h3 class="partner-tag">DUIS AUTE IRURE DOLOR</h3>
    <p class="partner-copy">Lorem ipsum dolor sit amet, consectetur adipiscing elit, sed do eiusmod tempor incid-idunt ut labore et dolore magna aliqua. Ut enim ad minim veniam, quis nostrud exer-citation ullamco laboris nisi ut aliquip ex ea commodo consequat.</p>
    <p class="partner-copy">Duis aute irure dolor in reprehenderit in voluptate velit esse cillum dolore eu fugiat nulla pariatur. Excepteur sint occaecat cupidatat non proident, sunt in culpa qui officia deserunt mollit anim id est laborum</p>
  </div>
  <div class="partner-photo" style="left:696px; top:481px" role="img" aria-label="Welder in protective mask with bright blue sparks"></div>

  <section class="contact-band"></section>
  <h1 class="section-title" style="top:856px">KONTAKT</h1>
  <div class="title-bar" style="top:902px"></div>
  <div class="contact-tab">Address</div>
  <div class="contact-details">
    <p>Ut enim ad minim veniam, quis nostrud</p>
    <p class="gap-lg">exercitation ullamco laboris</p>
    <p>nisi ut aliquip ex ea commodo</p>
    <p class="gap-lg">consequat.Consectetor Lorem Ipsum</p>
    <p class="gap-lg">Tel : <strong>+00 123456789</strong></p>
    <p class="gap-lg">E-mail : <strong>info@veltraprecision.com</strong></p>
  </div>

  <footer class="site-footer">
    <span>© 2018 Veltra Precision</span><span class="sep">/</span>
    <span>Impressum</span><span class="sep">/</span>
    <span>Datenschutzerklärung</span><span class="sep">/</span>
    <span>Haftungsausschluss</span>
  </footer>
</body>
</html>
```